Wine Bottle Label for Rosa Hartwell California Wine

This will be a wine bottle label. The wine is produced from grapes from our family farm. Images at bottom are some of same ones in high resolution

Rosa Hartwell
Reserve Pinot Noir
Clarksburg 2023
Estate Grown (in cursive)

We would like to have a view from above, looking down from the levee there is a slough (wing of a river) running behind it, it looks down over vineyards, a big wood barn, a giant Oak Tree beyond the barn. There are beautiful sunsets there in the distance. Many birds fly over the vineyards including small black birds (as shown in one photo). Please use what you can from these suggestions to make a label. We will need a small image for back label and wording on it.

Other font styles liked:
• Wine bottle fonts

Requirements
Must have
• Wording mentioned . An Oak Tree with images of the vines and a sunset
Nice to have
• Flock of black birds flying in the sky

```html
<!DOCTYPE html>
<html lang="en">
<head>
<meta charset="UTF-8">
<title>Rosa Hartwell – Reserve Pinot Noir Label</title>
<link href="https://fonts.googleapis.com/css2?family=Montserrat:wght@500;700&family=Pinyon+Script&display=swap" rel="stylesheet">
<style>
  :root {
    --page-bg: #ececea;
    --label-paper: #f6f5f4;
    --ink-slate: #2e3a40;
    --sky-rose: #f2b3a6;
    --sky-peach: #f7d9b8;
    --haze-lilac: #d9c8dc;
    --field-gold: #eacb95;
    --autumn-rust: #d98a6a;
    --shadow-teal: #7f95a0;
  }
  * { margin: 0; padding: 0; box-sizing: border-box; }
  html, body {
    width: 1200px;
    height: 1200px;
    overflow: hidden;
    background: var(--page-bg);
  }
  .canvas {
    width: 1200px;
    height: 1200px;
    display: flex;
    align-items: center;
    justify-content: center;
  }
  .wine-label {
    position: relative;
    width: 640px;
    height: 1000px;
    background: var(--label-paper);
    overflow: hidden;
    box-shadow: 0 6px 24px rgba(0,0,0,0.08);
  }
  .label-artwork {
    position: absolute;
    left: 0;
    right: 0;
    top: 180px;
    bottom: 90px;
    background:
      radial-gradient(ellipse 70% 18% at 55% 14%, rgba(242,179,166,0.55), transparent 70%),
      radial-gradient(ellipse 90% 35% at 50% 72%, rgba(217,138,106,0.55), transparent 70%),
      radial-gradient(ellipse 60% 20% at 30% 82%, rgba(127,149,160,0.45), transparent 70%),
      linear-gradient(180deg,
        rgba(246,245,244,0) 0%,
        rgba(247,217,184,0.55) 18%,
        rgba(217,200,220,0.45) 36%,
        rgba(234,203,149,0.6) 52%,
        rgba(217,138,106,0.55) 70%,
        rgba(234,203,149,0.45) 86%,
        rgba(246,245,244,0) 100%);
    -webkit-mask-image: linear-gradient(90deg, transparent 0%, #000 14%, #000 86%, transparent 100%);
    mask-image: linear-gradient(90deg, transparent 0%, #000 14%, #000 86%, transparent 100%);
  }
  .brand-name {
    position: absolute;
    top: 115px;
    left: 0;
    right: 0;
    text-align: center;
    font-family: 'Montserrat', sans-serif;
    font-weight: 700;
    font-size: 26px;
    letter-spacing: 0.62em;
    padding-left: 0.62em;
    color: var(--ink-slate);
    text-transform: uppercase;
  }
  .wine-title {
    position: absolute;
    top: 410px;
    left: 0;
    right: 0;
    text-align: center;
    font-family: 'Montserrat', sans-serif;
    font-weight: 700;
    font-size: 44px;
    letter-spacing: -0.01em;
    color: var(--ink-slate);
  }
  .wine-origin {
    position: absolute;
    top: 478px;
    left: 0;
    right: 0;
    text-align: center;
    font-family: 'Montserrat', sans-serif;
    font-weight: 500;
    font-size: 17px;
    letter-spacing: 0.42em;
    padding-left: 0.42em;
    color: var(--ink-slate);
    text-transform: uppercase;
  }
  .estate-mark {
    position: absolute;
    bottom: 58px;
    left: 0;
    right: 0;
    text-align: center;
    font-family: 'Pinyon Script', cursive;
    font-size: 52px;
    color: var(--ink-slate);
  }
</style>
</head>
<body>
  <main class="canvas">
    <section class="wine-label">
      <div class="label-artwork" role="img" aria-label="Soft watercolour view from the levee at sunset: a flock of birds in a rose and peach sky, hazy valley, autumn oaks, a wooden barn and fenced vineyard rows"></div>
      <p class="brand-name">Rosa Hartwell</p>
      <h1 class="wine-title">Reserve Pinot Noir</h1>
      <p class="wine-origin">Clarksburg 2023</p>
      <p class="estate-mark">Estate Grown</p>
    </section>
  </main>
</body>
</html>
```